Corporate Dinner Invite at Verolla for PMV

PMV is hosting a corporate dinner at the BRQ Conference and we need an email attachment invite for the event. Please use some images from this site for inspiration: https://www.verollaexample.com/fernparlor/

Invite Title:
Join us for dinner!

Event Details:
Tuesday, October 24th 2023 at 6:30pm
Verolla Chicago, Fern Parlor
347 W Harlow Ave, Chicago, IL 60622

Target Market(s)

Corporate Audience

Font styles to use
Script

Colors
0054AA
0677BA
7BADD7
CADEEF
E8F1F8

Requirements
Must have
• PMV logo, event date / time, event location details, photo(s) from Fern Parlor

```html
<!DOCTYPE html>
<html lang="en">
<head>
<meta charset="utf-8">
<title>PMV Dinner Invitation</title>
<link rel="stylesheet" href="https://fonts.googleapis.com/css2?family=Allura&family=EB+Garamond:wght@600&display=swap">
<style>
  :root {
    --blue-deep: #0054AA;
    --blue-mid: #0677BA;
    --blue-soft: #7BADD7;
    --blue-pale: #CADEEF;
    --blue-mist: #E8F1F8;
    --white: #ffffff;
    --bar-dark: #1c120c;
    --bar-warm: #4a2a16;
    --drink-amber: #e2a24a;
    --drink-gold: #f0c27a;
    --counter: #e9e6e2;
  }
  * { margin: 0; padding: 0; box-sizing: border-box; }
  html, body { width: 848px; height: 1200px; overflow: hidden; }
  body { background: var(--bar-dark); }

  .invite {
    position: relative;
    width: 848px;
    height: 1200px;
    overflow: hidden;
    font-family: "EB Garamond", Georgia, serif;
    color: var(--white);
  }

  .bar-backdrop {
    position: absolute; inset: 0;
    background:
      radial-gradient(ellipse at 8% 45%, rgba(190,90,40,.35), transparent 40%),
      radial-gradient(ellipse at 92% 55%, rgba(170,90,40,.3), transparent 40%),
      linear-gradient(180deg, var(--bar-dark), var(--bar-warm) 70%, var(--bar-dark));
  }

  .panel {
    position: absolute;
    left: 121px; top: 0;
    width: 594px; height: 1115px;
    background: linear-gradient(180deg, var(--blue-deep) 0%, var(--blue-mid) 45%, var(--blue-soft) 100%);
  }

  .brand {
    position: absolute;
    top: 68px; left: 0; width: 848px;
    display: flex; justify-content: center; align-items: center; gap: 14px;
  }
  .brand-mark { width: 34px; height: 34px; background: var(--white); }
  .brand-name { font-size: 60px; font-weight: 600; letter-spacing: 2px; line-height: 1; }

  .title {
    position: absolute; left: 0; width: 848px; text-align: center;
    font-family: "Allura", cursive;
    font-weight: 400; line-height: 1;
  }
  .title-join { top: 190px; font-size: 200px; }
  .title-for {
    position: absolute; top: 388px; left: 0; width: 848px; text-align: center;
    font-size: 46px; letter-spacing: 8px; line-height: 1;
  }
  .title-dinner { top: 400px; font-size: 200px; }

  .details {
    position: absolute; left: 0; width: 848px; text-align: center;
    font-size: 30px; letter-spacing: 1.5px; line-height: 40px;
  }
  .details-when { top: 594px; }
  .details-venue { top: 712px; }
  .details-address { top: 780px; }

  .rule {
    position: absolute; left: 190px; width: 462px; height: 2px;
    background: var(--white);
  }
  .rule-top { top: 693px; }
  .rule-bottom { top: 776px; }

  .cocktails {
    position: absolute; left: 0; top: 880px; width: 848px; height: 320px;
    background:
      linear-gradient(180deg, transparent 0%, transparent 72%, var(--counter) 74%, #cfcac4 100%),
      linear-gradient(90deg, rgba(226,162,74,.0) 6%, rgba(240,194,122,.75) 20%, rgba(226,162,74,.85) 40%, rgba(60,30,20,.85) 50%, rgba(226,162,74,.8) 68%, rgba(240,194,122,.8) 88%, rgba(226,162,74,0) 96%);
  }
</style>
</head>
<body>
  <main class="invite">
    <div class="bar-backdrop" role="img" aria-label="Softly blurred photo of a warmly lit bar with bottle shelves"></div>
    <div class="panel"></div>

    <div class="brand">
      <span class="brand-mark"></span>
      <span class="brand-name">PMV</span>
    </div>

    <h1>
      <span class="title title-join">Join Us</span>
      <span class="title-for">FOR</span>
      <span class="title title-dinner">Dinner!</span>
    </h1>

    <p class="details details-when">Tuesday, October 24th 2023<br>at 6:30pm</p>
    <div class="rule rule-top"></div>
    <p class="details details-venue">Verolla Chicago, Fern Parlor</p>
    <div class="rule rule-bottom"></div>
    <p class="details details-address">347 W Harlow Ave, Chicago,<br>IL 60622</p>

    <div class="cocktails" role="img" aria-label="Photo of a row of seven cocktails in crystal glasses on a marble bar counter"></div>
  </main>
</body>
</html>
```